High profile consulting company needs a Business Card Design

I need a business card design for a coaching /consulting company. We specialize in changing behaviors. Our services include therapy, workshops, life coaching, etc.

Check out our website to get a feel for our personality. www.tidewaterguidance.com

The new logo will be attached to the website soon, I have attached the new logo for your use on the business card.
Updates

I forgot to provide you with the company email under the "must have" section for the business card.  The website is:

 www.tidewaterguidance.com

I understand there's some trouble with the logo I uploaded.  I will try that again.  Thank you for your efforts.

Lauren

Thank you for some of your questions.  I prefer a one sided business card, and tend to like the white backgrounds.

I also made 2 small changes to the content.  

add MFT after the name:  Lauren Pettigrew, MFT

and the tag line needed more clarity once I saw it.  Please change it to:  Building better results through stronger connections and lasting new habits.

Thank you,
Lauren

Industry/Entity Type

Business

Requirements
Must have
• logo
Phone number: 321-555-0164
email: Lauren@tidewaterguidance.com
Lauren Pettigrew, MFT
President
Nice to have
• Building better results through stronger connections and lasting new habits.

```html
<!DOCTYPE html>
<html lang="en">
<head>
<meta charset="utf-8">
<title>Tidewater Guidance – Business Card</title>
<link href="https://fonts.googleapis.com/css2?family=Arimo:wght@400;700&display=swap" rel="stylesheet">
<style>
  :root {
    --backdrop: #232323;
    --card: #ffffff;
    --card-shade: #f1f1f1;
    --brand-green: #127a57;
    --ink: #2b2b2b;
    --mark-grey: #6e6e6e;
  }
  * { box-sizing: border-box; margin: 0; padding: 0; }
  html, body {
    width: 1200px; height: 944px; overflow: hidden;
    background: var(--backdrop);
    font-family: "Arimo", Arial, sans-serif;
  }
  .stage { position: relative; width: 1200px; height: 944px; }
  .card {
    position: absolute;
    width: 620px; height: 354px;
    border-radius: 26px;
    background: linear-gradient(160deg, var(--card) 60%, var(--card-shade));
    overflow: hidden;
  }
  .card--front { left: 90px; top: 90px; }
  .card--back { left: 490px; top: 500px; }

  .brand { display: flex; align-items: center; gap: 18px; }
  .brand__mark {
    flex: none; border-radius: 50%;
    background: var(--mark-grey);
    border: 6px solid var(--brand-green);
  }
  .brand__name {
    color: var(--brand-green);
    font-weight: 700;
    text-transform: uppercase;
    line-height: 1.02;
    letter-spacing: 0.02em;
  }
  .card--front .brand { position: absolute; left: 70px; top: 118px; }
  .card--front .brand__mark { width: 108px; height: 108px; }
  .card--front .brand__name { font-size: 50px; }

  .card--back .brand { position: absolute; left: 40px; top: 34px; }
  .card--back .brand__mark { width: 98px; height: 98px; }
  .card--back .brand__name { font-size: 44px; }

  .person { position: absolute; left: 40px; top: 160px; }
  .person__name { font-size: 25px; color: var(--ink); }
  .person__credential { font-size: 17px; color: var(--brand-green); }
  .person__title { font-size: 16px; color: var(--brand-green); margin-top: 3px; }

  .contact { position: absolute; left: 40px; top: 232px; list-style: none; }
  .contact__item {
    display: flex; align-items: center; gap: 12px;
    font-size: 17px; color: var(--ink); line-height: 22px;
  }
  .contact__icon { width: 16px; height: 16px; flex: none; }

  .tagline {
    position: absolute; left: 0; right: 0; bottom: 0; height: 44px;
    background: var(--brand-green);
    border-top: 3px solid #ffffff;
    box-shadow: 0 -2px 0 var(--brand-green);
    color: #ffffff;
    font-size: 12.5px; letter-spacing: 0.02em;
    text-transform: uppercase;
    white-space: nowrap;
    display: flex; align-items: center; justify-content: center;
  }
</style>
</head>
<body>
<main class="stage">
  <section class="card card--front" aria-label="Card front">
    <div class="brand">
      <span class="brand__mark"></span>
      <span class="brand__name">Tidewater<br>Guidance</span>
    </div>
  </section>

  <section class="card card--back" aria-label="Card back">
    <div class="brand">
      <span class="brand__mark"></span>
      <span class="brand__name">Tidewater<br>Guidance</span>
    </div>

    <div class="person">
      <p class="person__name">Lauren Pettigrew<span class="person__credential">, MFT</span></p>
      <p class="person__title">President</p>
    </div>

    <ul class="contact">
      <li class="contact__item">
        <svg class="contact__icon" viewBox="0 0 16 16" aria-hidden="true">
          <path d="M4 1.5l2.2 2.8-1.3 1.6c.8 1.8 2.2 3.3 4 4.2l1.6-1.3 2.8 2.2-1.4 2.4C7.4 13 3 8.6 1.6 3z" fill="none" stroke="#2b2b2b" stroke-width="1.4"/>
        </svg>
        321-555-0164
      </li>
      <li class="contact__item">
        <svg class="contact__icon" viewBox="0 0 16 16" aria-hidden="true">
          <rect x="1" y="3.5" width="14" height="9" rx="1.5" fill="#2b2b2b"/>
          <path d="M1.5 4l6.5 5 6.5-5" fill="none" stroke="#fff" stroke-width="1.2"/>
        </svg>
        Lauren@tidewaterguidance.com
      </li>
      <li class="contact__item">
        <svg class="contact__icon" viewBox="0 0 16 16" aria-hidden="true">
          <circle cx="8" cy="8" r="7" fill="#2b2b2b"/>
        </svg>
        www.tidewaterguidance.com
      </li>
    </ul>

    <p class="tagline">Building better results through stronger connections and lasting new habits</p>
  </section>
</main>
</body>
</html>
```